BRINTEX Hardware needs a Flyer Designed

We need a flyer designed for a marketing strategy that is to be launched by BRINTEX. As it is for our hardware division, our logo should go unto the flyer. We are offering to our customers financing on items from $5000 up to $35000. Here are some key words that you may want to include; "building or revovating? you pick the job we've got the financing." The flyer should reflect some sort of home construction and should be very attractive and vibrant. On the flyer it should also state that it's "hassle-free" and; "no down payment", "no collateral", "affordable monthly payments".

Must Haves [en ]: The companies logo. Also it must state the address of the company and contact info which is; 47 Fellowby Lane Penal, Trinidad. Tel: 868-47-BRINTEX. Email must also be listed: info@brintexgroup.example.

Nice To Haves [en ]: Good quality graphics. something that is captivating and that will hold the attention of our audience.

Should Not Haves [en ]: Should not be too busy.

Requirements
Must have
• The companies logo. Also it must state the address of the company and contact info which is; 47 Fellowby Lane Penal, Trinidad. Tel: 868-47-BRINTEX. Email must also be listed: info@brintexgroup.example.
Nice to have
• Good quality graphics. something that is captivating and that will hold the attention of our audience.
Should not have
• Should not be too busy.

```html
<!DOCTYPE html>
<html lang="en">
<head>
<meta charset="utf-8">
<title>BRINTEX Hardware – Building or Renovating?</title>
<link rel="stylesheet" href="https://fonts.googleapis.com/css2?family=Oswald:wght@500&family=Roboto+Condensed:wght@400;700&display=swap">
<style>
  :root {
    --navy: #1f2b5e;
    --red: #ea2d35;
    --sky: #1b9fe0;
    --white: #ffffff;
    --ink: #2a2a2a;
    --illus-light: #eef0f3;
    --illus-mid: #c9ccd3;
  }
  html, body { margin: 0; padding: 0; overflow: hidden; background: var(--white); }
  .flyer {
    position: relative;
    width: 846px;
    height: 1200px;
    overflow: hidden;
    background: var(--navy);
    font-family: "Roboto Condensed", "Arial Narrow", sans-serif;
    color: var(--white);
  }
  .hero-shapes { position: absolute; left: 0; top: 0; }
  .brand-disc {
    position: absolute;
    left: 542px; top: 293px;
    width: 240px; height: 240px;
    border-radius: 50%;
    background: var(--white);
    display: flex; align-items: center; justify-content: center;
  }
  .brand-name {
    font-family: "Roboto Condensed", "Arial Narrow", sans-serif;
    font-weight: 700;
    font-size: 50px;
    letter-spacing: 1px;
    color: var(--navy);
  }
  .headline {
    position: absolute;
    left: 0; top: 612px; width: 846px;
    margin: 0;
    text-align: center;
    font-family: "Oswald", "Arial Narrow", sans-serif;
    font-weight: 500;
    font-size: 64px;
    letter-spacing: 1px;
    line-height: 1;
  }
  .tagline-band {
    position: absolute;
    left: 72px; top: 704px;
    width: 696px; height: 57px;
    background: var(--sky);
    display: flex; align-items: center; justify-content: center;
    font-weight: 700;
    font-size: 35px;
  }
  .offer {
    position: absolute;
    left: 0; top: 800px; width: 846px;
    margin: 0;
    text-align: center;
    font-weight: 700;
    font-size: 40px;
    line-height: 54px;
  }
  .offer .amount { color: var(--sky); }
  .benefits {
    position: absolute;
    left: 0; top: 941px;
    width: 846px; height: 136px;
    background: var(--red);
  }
  .benefit {
    position: absolute;
    display: flex; align-items: center;
    font-size: 30px;
  }
  .benefit svg { margin-right: 20px; }
  .benefit--hassle { left: 117px; top: 15px; }
  .benefit--downpayment { left: 362px; top: 15px; }
  .benefit--collateral { left: 117px; top: 77px; }
  .benefit--monthly { left: 362px; top: 77px; }
  .contact {
    position: absolute;
    left: 0; top: 1077px;
    width: 846px; height: 123px;
    background: var(--white);
    color: var(--ink);
    font-size: 23px;
  }
  .contact-address { position: absolute; left: 64px; top: 21px; }
  .contact-lines { position: absolute; left: 62px; top: 62px; display: flex; align-items: center; }
  .contact-divider { display: inline-block; width: 2px; height: 28px; background: var(--red); margin: 0 18px; }
  .social { position: absolute; left: 620px; top: 66px; display: flex; gap: 16px; }
  .social span { width: 24px; height: 24px; border-radius: 50%; background: var(--navy); display: block; }
</style>
</head>
<body>
<div class="flyer">
  <svg class="hero-shapes" width="846" height="600" viewBox="0 0 846 600">
    <defs>
      <linearGradient id="illusTone" x1="0" y1="0" x2="1" y2="1">
        <stop offset="0" stop-color="var(--illus-light)"/>
        <stop offset="1" stop-color="var(--illus-mid)"/>
      </linearGradient>
    </defs>
    <path class="outer-swoosh" d="M0 0 H705 C680 210 600 410 390 515 C250 580 100 590 0 575 Z" fill="var(--white)"/>
    <path class="inner-field" d="M0 0 H665 C640 190 570 370 380 470 C250 535 110 545 0 525 Z" fill="var(--white)"/>
    <path class="illustration" role="img" aria-label="3D model of a white house with a red roof under construction, resting on rolled blueprints with a tape measure, pencil and eraser" d="M20 40 H600 C585 190 520 340 370 430 C260 495 120 505 20 480 Z" fill="url(#illusTone)"/>
    <path class="red-swoosh" d="M645 0 H690 C720 240 620 450 300 560 C560 440 670 250 645 0 Z" fill="var(--red)"/>
    <path class="sky-swoosh" d="M792 0 H808 C800 110 770 200 720 270 C760 190 785 100 792 0 Z" fill="var(--sky)"/>
  </svg>

  <div class="brand-disc"><span class="brand-name">BRINTEX</span></div>

  <h1 class="headline">BUILDING OR RENOVATING?</h1>
  <div class="tagline-band">You Pick the Job, We’ve got the Finances!</div>
  <p class="offer">Customers financing on items<br>from <span class="amount">$5000</span> up to <span class="amount">$35000</span></p>

  <div class="benefits">
    <div class="benefit benefit--hassle">
      <svg width="34" height="34" viewBox="0 0 34 34"><circle cx="17" cy="17" r="15" fill="var(--navy)"/><path d="M9 17 L15 23 L29 5" stroke="var(--white)" stroke-width="4" fill="none" stroke-linecap="round"/></svg>Hassle–free</div>
    <div class="benefit benefit--downpayment">
      <svg width="34" height="34" viewBox="0 0 34 34"><circle cx="17" cy="17" r="15" fill="var(--navy)"/><path d="M9 17 L15 23 L29 5" stroke="var(--white)" stroke-width="4" fill="none" stroke-linecap="round"/></svg>No Down–payment</div>
    <div class="benefit benefit--collateral">
      <svg width="34" height="34" viewBox="0 0 34 34"><circle cx="17" cy="17" r="15" fill="var(--navy)"/><path d="M9 17 L15 23 L29 5" stroke="var(--white)" stroke-width="4" fill="none" stroke-linecap="round"/></svg>No Collateral</div>
    <div class="benefit benefit--monthly">
      <svg width="34" height="34" viewBox="0 0 34 34"><circle cx="17" cy="17" r="15" fill="var(--navy)"/><path d="M9 17 L15 23 L29 5" stroke="var(--white)" stroke-width="4" fill="none" stroke-linecap="round"/></svg>Affordable Monthly Payments</div>
  </div>

  <footer class="contact">
    <div class="contact-address">47 Fellowby Lane Penal, Trinidad</div>
    <div class="contact-lines">
      <span>T. 868–47–BRINTEX</span>
      <span class="contact-divider"></span>
      <span>E. info@brintexgroup.example</span>
    </div>
    <div class="social"><span></span><span></span><span></span></div>
  </footer>
</div>
</body>
</html>
```